Business Card Design Project

A double sided business card for presentation to business leaders in corporate.

Target Market(s)

Corporate, business professionals, HR

Industry/Entity Type

Business

Requirements
Must have
• FRONT

Logo

www.brightlanecoaching.com.au

BACK

Mara Pollen-Drew
Director

+ 61 (0) 418 536 204
mara@brightlanecoaching.com.au
www.brightlanecoaching.com.au

Impact through energy and employee engagement

("ripples" of logo, bottom corner)

Must be:
- double sided
size: 86 x 54mm
supplied as one pdf with crop marks shown (+- 1mm, with 2-3 mm bleed)

```html
<!DOCTYPE html>
<html lang="en">
<head>
<meta charset="utf-8">
<title>Brightlane Coaching – Business Card Options</title>
<link rel="stylesheet" href="https://fonts.googleapis.com/css2?family=Questrial&display=swap">
<style>
  :root {
    --stage: #b3946a;
    --label: #222222;
    --card-white: #ffffff;
    --plum: #7a2a66;
    --plum-light: #93417d;
    --plum-dark: #6a1f57;
    --charcoal: #4a4a4a;
    --charcoal-faint: #575757;
    --ink: #3d3d3d;
    --white: #ffffff;
  }
  * { box-sizing: border-box; margin: 0; padding: 0; }
  html, body {
    width: 1200px; height: 788px; overflow: hidden;
    background: var(--stage);
    font-family: "Questrial", "Century Gothic", sans-serif;
  }
  .sheet { position: relative; width: 1200px; height: 788px; }

  .side-label {
    position: absolute; width: 200px; text-align: center;
    font-size: 20px; color: var(--label);
  }

  .card {
    position: absolute; width: 510px; height: 319px;
    border-radius: 20px; overflow: hidden;
    box-shadow: 0 3px 8px rgba(0,0,0,0.35);
  }
  .card--white { background: var(--card-white); }
  .card--charcoal { background: var(--charcoal); }
  .card--plum { background: linear-gradient(90deg, var(--plum-light), var(--plum-dark)); }

  .wordmark {
    position: absolute; display: flex; align-items: flex-start; gap: 12px;
  }
  .wordmark__dot { border-radius: 50%; flex: none; }
  .wordmark__name { line-height: 0.92; letter-spacing: -1px; }
  .wordmark__name span { display: block; }
  .wordmark__name span + span { text-align: right; }

  .name-band {
    position: absolute; left: 0; top: 183px; width: 437px; height: 35px;
    background: linear-gradient(90deg, var(--plum-light), var(--plum-dark));
    color: var(--white); font-size: 16px; line-height: 35px; padding-left: 122px;
  }
  .name-band small { font-size: 13px; }
  .grey-tab {
    position: absolute; left: 444px; top: 183px; width: 66px; height: 35px;
    background: var(--charcoal);
  }
  .contact-list {
    position: absolute; left: 144px; top: 247px; list-style: none;
    font-size: 13px; color: var(--ink); line-height: 18.5px;
  }
  .contact-list li { display: flex; align-items: center; gap: 6px; }
  .contact-list svg { width: 10px; height: 10px; flex: none; }

  .web-spaced {
    position: absolute; left: 0; width: 100%; text-align: center;
    font-size: 13px; letter-spacing: 3.2px;
  }
  .web-plain {
    position: absolute; left: 29px; bottom: 18px;
    font-size: 13px; color: var(--white);
  }
  .faint-circle {
    position: absolute; left: 240px; top: 20px; width: 250px; height: 250px;
    border-radius: 50%; border: 3px solid var(--charcoal-faint);
  }
</style>
</head>
<body>
<main class="sheet">

  <div class="side-label" style="left:220px; top:19px;">Front</div>
  <div class="side-label" style="left:793px; top:19px;">Back - 1</div>
  <div class="side-label" style="left:225px; top:404px;">Back - 2</div>
  <div class="side-label" style="left:797px; top:404px;">Back - 3</div>

  <!-- Front -->
  <section class="card card--white" style="left:70px; top:50px;" aria-label="Card front">
    <div class="wordmark" style="left:88px; top:38px;">
      <span class="wordmark__dot" style="width:22px; height:22px; background:var(--plum); margin-top:28px;"></span>
      <div class="wordmark__name" style="font-size:48px; color:var(--plum);">
        <span>brightlane</span><span>coaching</span>
      </div>
    </div>
    <div class="name-band">Mara Pollen-Drew, <small>Director</small></div>
    <div class="grey-tab"></div>
    <ul class="contact-list">
      <li>
        <svg viewBox="0 0 10 10"><circle cx="5" cy="5" r="4.5" fill="none" stroke="#7a2a66"/><path d="M3 3 L4 2.5 L4.6 4 L4 4.5 Q4.6 5.8 5.6 6 L6.1 5.4 L7.5 6 L7 7 Q4 7.5 3 3Z" fill="#7a2a66"/></svg>
        + 61 (0) 418 536 204
      </li>
      <li>
        <svg viewBox="0 0 10 10"><rect x="0.5" y="2" width="9" height="6.5" fill="none" stroke="#7a2a66"/><path d="M0.5 2 L5 6 L9.5 2" fill="none" stroke="#7a2a66"/></svg>
        mara@brightlanecoaching.com.au
      </li>
      <li>
        <svg viewBox="0 0 10 10"><circle cx="5" cy="5" r="4.5" fill="#7a2a66"/></svg>
        www.brightlanecoaching.com.au
      </li>
    </ul>
  </section>

  <!-- Back 1 -->
  <section class="card card--white" style="left:640px; top:50px; width:507px;" aria-label="Card back, white">
    <div class="wordmark" style="left:78px; top:62px;">
      <span class="wordmark__dot" style="width:28px; height:28px; background:var(--plum); margin-top:40px;"></span>
      <div class="wordmark__name" style="font-size:72px; color:var(--plum);">
        <span>brightlane</span><span>coaching</span>
      </div>
    </div>
    <div class="web-spaced" style="top:276px; color:var(--ink);">www.brightlanecoaching.com.au</div>
  </section>

  <!-- Back 2 -->
  <section class="card card--charcoal" style="left:70px; top:436px;" aria-label="Card back, charcoal">
    <div class="faint-circle"></div>
    <div class="wordmark" style="left:22px; top:70px;">
      <span class="wordmark__dot" style="width:18px; height:18px; background:var(--white); margin-top:24px;"></span>
      <div class="wordmark__name" style="font-size:62px; color:var(--white);">
        <span>brightlane</span>
      </div>
    </div>
    <div class="web-plain">www.brightlanecoaching.com.au</div>
  </section>

  <!-- Back 3 -->
  <section class="card card--plum" style="left:640px; top:436px; width:507px;" aria-label="Card back, plum">
    <div class="wordmark" style="left:78px; top:70px;">
      <span class="wordmark__dot" style="width:26px; height:26px; background:var(--white); margin-top:36px;"></span>
      <div class="wordmark__name" style="font-size:66px; color:var(--white);">
        <span>brightlane</span><span>coaching</span>
      </div>
    </div>
    <div class="web-spaced" style="top:277px; color:var(--white);">www.brightlanecoaching.com.au</div>
  </section>

</main>
</body>
</html>
```